Tall Heron Vodka

We are launching a new mainstream Vodka brand "Tall Heron" to take on big brands. China will be first market. The category norms seems to be Red and Black on a clear bottle and we would expect some red but does not need to be entirely red. The design would need to work on both clear (Valdorin) and frosted (Pale Finch) style bottles. In the future we will have gold heron, silver heron, platinum heron and diamond heron for more premium variants.

Target Market(s)

China

Industry/Entity Type

Alcohol

Colors
EB3D1F
EC4F4E
F09395
F8D3D4
FCEDEE

Requirements
Must have
• Space for Chinese language as well ad English
Nice to have
• Energetic, Engaging
Should not have
• Not stereotypes of photo of bad looking bear. Good looking bear, light not heavy.

```html
<!DOCTYPE html>
<html lang="en">
<head>
<meta charset="utf-8">
<title>Tall Heron Vodka – Identity and Label</title>
<link rel="stylesheet" href="https://fonts.googleapis.com/css2?family=Encode+Sans+Condensed:wght@500&family=Montserrat:wght@600&family=Lora:wght@700&display=swap">
<style>
  :root {
    --ink: #3d3d3d;
    --band: #3a3a3a;
    --red: #eb3d1f;
    --red-soft: #ec4f4e;
    --left-bg: #efefef;
    --right-bg: #f6f6f6;
    --label-bg: #e9e9ea;
    --light-band: #f4f4f4;
    --paper: #ffffff;
  }
  html, body {
    margin: 0;
    width: 1200px;
    height: 1000px;
    overflow: hidden;
  }
  .canvas {
    position: relative;
    width: 1200px;
    height: 1000px;
    background: var(--right-bg);
  }
  .logo-panel {
    position: absolute;
    left: 0; top: 0;
    width: 441px; height: 1000px;
    background: var(--left-bg);
  }
  .lockup {
    position: absolute;
    left: 60px;
    width: 320px;
    display: flex;
    align-items: center;
    gap: 16px;
  }
  .lockup--primary { top: 180px; }
  .lockup--secondary { top: 680px; }
  .lockup__mark {
    width: 54px; height: 54px;
    border-radius: 50%;
    background: var(--ink);
    flex: none;
  }
  .lockup__name {
    font-family: "Encode Sans Condensed", sans-serif;
    font-weight: 500;
    font-size: 58px;
    line-height: 1;
    color: var(--ink);
    white-space: nowrap;
  }
  .label {
    position: absolute;
    top: 300px;
    width: 168px;
    height: 540px;
    background: var(--label-bg);
    overflow: hidden;
  }
  .label--front { left: 639px; }
  .label--back { left: 846px; }
  .label svg { position: absolute; inset: 0; }
  .front__brand {
    position: absolute;
    left: 0; right: 0; top: 140px;
    display: flex;
    align-items: center;
    justify-content: center;
    gap: 6px;
  }
  .front__brand .lockup__mark { width: 16px; height: 16px; }
  .front__brand .lockup__name { font-size: 24px; }
  .front__product {
    position: absolute;
    left: 0; right: 0; top: 303px;
    height: 60px;
    display: flex;
    align-items: center;
    justify-content: center;
    font-family: "Montserrat", sans-serif;
    font-weight: 600;
    font-size: 27px;
    letter-spacing: 1px;
    color: var(--red-soft);
  }
  .front__volume {
    position: absolute;
    left: 0; right: 0; bottom: 18px;
    text-align: center;
    font-family: "Montserrat", sans-serif;
    font-weight: 600;
    font-size: 8px;
    color: var(--ink);
  }
  .back__copy {
    position: absolute;
    left: 24px; right: 14px; top: 222px;
    margin: 0;
    text-align: center;
    font-family: "Lora", serif;
    font-weight: 700;
    font-size: 7.2px;
    line-height: 1.33;
    color: var(--paper);
  }
</style>
</head>
<body>
<main class="canvas">
  <section class="logo-panel">
    <div class="lockup lockup--primary">
      <span class="lockup__mark"></span>
      <span class="lockup__name">Tall Heron</span>
    </div>
    <div class="lockup lockup--secondary">
      <span class="lockup__mark"></span>
      <span class="lockup__name">Tall Heron</span>
    </div>
  </section>

  <section class="label label--front">
    <svg width="168" height="540" viewBox="0 0 168 540">
      <polygon points="0,150 168,48 168,190 0,300" fill="var(--light-band)"/>
      <polygon points="0,420 168,345 168,395 0,480" fill="var(--band)"/>
      <rect x="0" y="303" width="168" height="60" fill="var(--band)"/>
    </svg>
    <div class="front__brand">
      <span class="lockup__mark"></span>
      <span class="lockup__name">Tall Heron</span>
    </div>
    <div class="front__product">VODKA</div>
    <div class="front__volume">750ML / 40% ALC</div>
  </section>

  <section class="label label--back">
    <svg width="168" height="540" viewBox="0 0 168 540">
      <polygon points="0,250 168,120 168,330 60,430 0,470" fill="var(--band)"/>
    </svg>
    <p class="back__copy">Lorem ipsum dolor sit amet, consectetur adipiscing elit. Aenean auctor congue convallis. Aenean vel ante sed mi dictum porttitor a nec urna. Donec rutrum eros quam, at tristique dolor faucibus et. Mauris sed condimentum neque. Morbi sit amet justo eu elit iaculis congue. Pellentesque ac nisl hendrerit, pulvinar risus sit amet, mollis nisl.</p>
  </section>
</main>
</body>
</html>
```